DL SIZED ONE SIDED BROCHURE FOR CLEANING AND GARDENING SERVICE

business name: Q&T property services
services provided: Strata cleaning,lawn mowing,hedge trimming,garden maintainance,lawn repair,weed spraying/removal, rubbish removal.
10 years experience and fully insured.
obligation free quotes.
phone number:contact vince 0427093516
email: qtpropertyservices@mailbox-example.net
slogan: when quality matters ring Q&T
Q&T logo would be nice but not essential
DL size in inches: 3.9in × 8.2in
DL size in millimetres: 100mm × 210mm
DL size in centimetres: 10cm x 21cm
Updates
doing good guys no suggestions except being original
Target Market(s)
real estate agents, private home owners, contractors.
Industry/Entity Type
Business
Look and feel
Each slider illustrates characteristics of the customer's brand and the style your logo design should communicate.

```html
<!DOCTYPE html>
<html lang="en">
<head>
<meta charset="utf-8">
<title>Q&amp;T Property Services – DL Brochure</title>
<link rel="stylesheet" href="https://fonts.googleapis.com/css2?family=Arimo:ital,wght@0,400;0,700;1,700&display=swap">
<style>
  :root {
    --leaf-deep: #14480f;
    --leaf-mid: #2f7a22;
    --swoosh-light: #8cc63f;
    --sun-yellow: #f4e21a;
    --quote-red: #c8161d;
    --paper-white: #ffffff;
    --timber: #8a5a2b;
    --timber-dark: #5e3a17;
  }
  * { margin: 0; padding: 0; box-sizing: border-box; }
  html, body { width: 1200px; height: 576px; overflow: hidden; background: #ffffff; }
  .brochure {
    position: relative;
    width: 1200px;
    height: 576px;
    overflow: hidden;
    font-family: "Arimo", Arial, sans-serif;
    background: linear-gradient(180deg, var(--leaf-mid) 0%, var(--leaf-deep) 70%, #2b5a1a 100%);
  }
  .garden-scene-top {
    position: absolute; right: 0; top: 0; width: 700px; height: 330px;
    background: linear-gradient(160deg, #a8cde8 0%, #6fa85a 30%, #c0508a 55%, #3e7a2c 80%);
    clip-path: polygon(22% 0, 100% 0, 100% 100%, 40% 100%, 8% 40%);
  }
  .garden-bed-bottom {
    position: absolute; left: 0; bottom: 0; width: 1200px; height: 190px;
    background: linear-gradient(180deg, rgba(60,110,40,0) 0%, #5b7f3a 35%, #3d6a2a 70%, #6a5a3a 100%);
  }
  .swoosh { position: absolute; left: 0; top: 0; width: 1200px; height: 576px; }
  .quote-pill {
    position: absolute; left: 0; top: 76px; width: 218px; height: 40px;
    background: var(--quote-red); color: var(--paper-white);
    border-radius: 0 20px 20px 0; border: 2px solid var(--paper-white); border-left: none;
    font-weight: 700; font-size: 17px; line-height: 36px; padding-left: 14px;
  }
  .brand { position: absolute; left: 234px; top: 58px; }
  .brand-name {
    display: flex; align-items: center; gap: 12px;
    color: var(--paper-white); font-weight: 700; font-size: 34px; line-height: 1;
  }
  .brand-dot { width: 28px; height: 28px; border-radius: 50%; background: var(--paper-white); }
  .brand-slogan {
    margin-top: 6px; color: var(--sun-yellow);
    font-weight: 700; font-style: italic; font-size: 15px;
  }
  .services {
    position: absolute; left: 80px; top: 140px; width: 660px;
    text-align: center; color: var(--sun-yellow);
    font-weight: 700; font-size: 26px; line-height: 36px;
    text-shadow: 1px 1px 2px rgba(0,0,0,0.5);
    z-index: 2;
  }
  .experience-sign { position: absolute; left: 0; top: 340px; width: 360px; height: 96px; }
  .experience-sign svg { position: absolute; inset: 0; }
  .experience-years {
    position: absolute; left: 16px; top: 8px;
    color: var(--paper-white); font-weight: 700; font-size: 70px; line-height: 80px;
  }
  .experience-text {
    position: absolute; left: 104px; top: 22px;
    color: var(--sun-yellow); font-weight: 700; font-size: 22px; line-height: 26px;
  }
  .contact { position: absolute; left: 440px; top: 356px; z-index: 3; }
  .contact-name, .contact-phone {
    color: var(--sun-yellow); font-weight: 700;
    text-shadow: 2px 2px 3px rgba(0,0,0,0.5);
  }
  .contact-name { font-size: 46px; line-height: 56px; }
  .contact-phone { font-size: 48px; line-height: 58px; }
  .contact-email {
    margin-top: 14px; color: var(--paper-white); font-weight: 700; font-size: 13px;
    white-space: nowrap;
  }
  .photo-circle {
    position: absolute; border-radius: 50%; border: 6px solid var(--paper-white);
    box-shadow: 0 2px 8px rgba(0,0,0,0.4);
  }
  .photo-circle--garden {
    left: 790px; top: 344px; width: 250px; height: 250px;
    background: radial-gradient(circle at 40% 60%, #e0a040 0%, #6aa040 40%, #2e6a25 100%);
  }
  .photo-circle--estate {
    left: 964px; top: 230px; width: 236px; height: 236px;
    background: linear-gradient(180deg, #cfe0ef 0%, #b9c6b0 35%, #5c9a3c 60%, #d23a3a 100%);
  }
</style>
</head>
<body>
<main class="brochure">
  <div class="garden-scene-top" role="img" aria-label="Photo of a flowering garden with azaleas and trees"></div>
  <div class="garden-bed-bottom" role="img" aria-label="Photo of a planted garden bed with grasses and shrubs"></div>

  <svg class="swoosh" viewBox="0 0 1200 576" aria-hidden="true">
    <path d="M0 0 H560 C470 60 420 120 300 150 C200 172 90 160 0 150 Z" fill="var(--leaf-deep)" opacity="0.9"/>
    <path d="M0 150 C120 170 260 170 360 140 C470 105 520 40 600 0 H640 C560 60 500 150 380 180 C250 210 110 200 0 190 Z" fill="var(--swoosh-light)"/>
  </svg>

  <div class="quote-pill">Obligation Free Quotes</div>

  <div class="brand">
    <div class="brand-name"><span class="brand-dot"></span>Q&amp;T Property Services</div>
    <div class="brand-slogan">When quality matters ring Q&amp;T</div>
  </div>

  <p class="services">
    Strata cleaning, lawn mowing,<br>
    hedge trimming, garden maintainance,<br>
    lawn repair, weed spraying/removal,<br>
    rubbish removal.
  </p>

  <div class="experience-sign">
    <svg viewBox="0 0 360 96" aria-hidden="true">
      <path d="M0 6 H320 L356 48 L320 90 H0 Z" fill="var(--timber)" stroke="var(--timber-dark)" stroke-width="4"/>
    </svg>
    <span class="experience-years">10</span>
    <span class="experience-text">years experience<br>and fully insured</span>
  </div>

  <div class="photo-circle photo-circle--estate" role="img" aria-label="Photo of formal garden beds in front of a manor house"></div>
  <div class="photo-circle photo-circle--garden" role="img" aria-label="Photo of a landscaped garden path with flowers"></div>

  <div class="contact">
    <div class="contact-name">Vince</div>
    <div class="contact-phone">0427093516</div>
    <div class="contact-email">email: qtpropertyservices@mailbox-example.net</div>
  </div>
</main>
</body>
</html>
```